Pagina Casalúmen

The Casalúmen is a company dealing with leasing and selling real estate. The current site can be accessed at www.casalumen.com.br. We intend to redesign the look of the site and for that we would like to redesign the home page and the page with information and pictures of the property. The homepage should maintain the characteristics of the current common design simple, short and straightforward. The page with the data of the properties should be accessed with two changes page as it is currently running. The search from the map by region and should be maintained.
The page containing the information of the property will provide a total of 15 small pictures that when clicked will appear in larger size. The colors to be used should be orange, blue, black and white. The map can be maintained in the current colors.
Updates

Payment guaranteed. Deadline for submission of designs April 27.

Industry/Entity Type

Real Estate

Requirements
Must have
• Search by map regions and search box
address
keep colors from the current page
phones
clean look
Nice to have
• clean look
Should not have
• We like the current page. We just want to make it compatible with modern and new design trends and monitors.

```html
<!DOCTYPE html>
<html lang="en">
<head>
<meta charset="utf-8">
<title>Casalúmen – Real Estate</title>
<link href="https://fonts.googleapis.com/css2?family=Ubuntu:wght@400;500;700&family=Arimo:wght@400;700&display=swap" rel="stylesheet">
<style>
:root{
  --orange:#f58220;
  --orange-dark:#e0700f;
  --purple:#4b4668;
  --purple-dark:#3d3957;
  --ink:#333;
  --grey-bg:#efefef;
  --white:#fff;
  --link:#1b4f9c;
}
*{box-sizing:border-box;margin:0;padding:0}
html,body{width:960px;height:1200px;overflow:hidden}
body{position:relative;background:var(--grey-bg);font-family:'Arimo',Arial,sans-serif;color:var(--ink)}
.abs{position:absolute}
.top-band{left:0;top:0;width:960px;height:410px;background:var(--orange)}
.page-shape{left:0;top:0}
.utility-links{right:84px;top:11px;font-size:10px;color:var(--white);font-family:'Arimo',sans-serif;letter-spacing:.3px}
.utility-links span{margin:0 6px}
.phones{left:734px;top:40px;font-family:'Ubuntu',sans-serif;font-size:14.5px;color:var(--white);line-height:18px;text-align:right}
.phone-icon{left:680px;top:37px}
.brand{left:104px;top:68px;font-family:'Ubuntu',sans-serif;font-weight:700;font-size:34px;color:var(--purple)}
.main-nav{left:89px;top:130px;width:777px;height:38px;background:var(--purple);border-radius:8px;display:flex;align-items:center;padding:0 6px;font-family:'Ubuntu',sans-serif;font-size:10.5px;color:var(--white)}
.main-nav a{color:inherit;text-decoration:none;padding:0 14px;height:26px;line-height:26px;border-right:1px solid #6a6585;white-space:nowrap}
.main-nav a:last-child{border-right:0}
.main-nav .active{background:var(--orange);border-radius:6px;border:1px solid #ffa050;padding:0 8px}
.hero{left:95px;top:178px;width:766px;height:296px;background:linear-gradient(180deg,#24305c 0%,#3b4a6e 30%,#c9a66b 55%,#6b4a2a 75%,#2a4660 100%)}
.hero-shadow{left:130px;top:474px;width:700px;height:14px;background:radial-gradient(ellipse at center top,rgba(0,0,0,.25),transparent 70%)}
.welcome-title{left:118px;top:540px;font-family:'Ubuntu',sans-serif;font-size:24px;color:var(--purple);font-weight:500}
.welcome-title .w{font-size:38px}
.welcome-title em{font-style:normal;color:var(--orange)}
.dotted{border-top:1px dotted #aaa}
.welcome-text{left:110px;top:592px;width:482px;font-size:10px;line-height:17.6px;text-align:justify}
.welcome-text p+p{margin-top:17.6px}
.contact-line{left:104px;top:752px;font-family:'Ubuntu',sans-serif;white-space:nowrap}
.contact-line .big{font-size:27px;color:var(--orange)}
.contact-line .small{font-family:'Arimo',sans-serif;font-size:10px;color:var(--ink);margin:0 8px 0 0}
.contact-line .mail{font-size:14px;color:var(--orange);margin-left:4px}
.map-box{left:618px;top:514px;width:243px;height:265px;border:2px solid var(--white)}
.map-box h3{font-family:'Ubuntu',sans-serif;font-weight:400;font-size:14px;color:var(--purple);text-align:center;margin-top:8px}
.map-box h3 b{color:var(--orange)}
.map{left:25px;top:32px;width:190px;height:224px;background:linear-gradient(135deg,#6ab7e6 0%,#9bd0ea 40%,#e9d8a0 60%,#6ab7e6 100%)}
.divider{left:90px;top:818px;width:790px;height:1px;background:linear-gradient(90deg,transparent,#ccc,transparent)}
.col-title{font-family:'Ubuntu',sans-serif;font-weight:400;font-size:21px;color:#444;white-space:nowrap}
.col-sep{width:1px;top:848px;height:240px;background:linear-gradient(180deg,transparent,#d5d5d5,transparent)}
.col-text{font-size:9.6px;line-height:16px;letter-spacing:.3px;text-align:justify}
.col-text b{color:#111}
.details{font-size:9px;font-weight:700;color:var(--link)}
.company-photo{left:104px;top:894px;width:219px;height:98px;background:var(--white);border:1px solid #ddd;padding:4px}
.company-photo div{width:100%;height:100%;background:linear-gradient(90deg,#9fb6cf,#e3d7c8 55%,#8aa2bd)}
.radio{left:637px;font-size:9.6px;font-weight:700;display:flex;align-items:center}
.radio i{width:9px;height:9px;border:1px solid #999;border-radius:50%;background:#f7f7f7;margin-right:8px;display:inline-block;position:relative}
.radio i.on::after{content:"";position:absolute;left:2px;top:2px;width:3px;height:3px;border-radius:50%;background:var(--link)}
.select{left:631px;top:1003px;width:232px;height:27px;background:var(--white);border:1px solid #ddd;border-radius:14px;font-size:9.6px;line-height:25px;padding-left:14px}
.select::after{content:"";position:absolute;right:12px;top:11px;border:4px solid transparent;border-top:5px solid #444}
.btn-search{left:790px;top:1056px;width:74px;height:24px;background:var(--purple);border:2px solid #8a86a6;border-radius:12px;color:var(--white);font-size:10px;font-weight:700;display:flex;align-items:center;padding-left:6px;gap:6px}
.footer{left:0;top:1118px;width:960px;height:82px;background:var(--purple);color:var(--white);font-size:10px;line-height:17.6px;text-align:center;padding-top:15px}
</style>
</head>
<body>
<div class="abs top-band"></div>
<svg class="abs page-shape" width="960" height="410" viewBox="0 0 960 410" aria-hidden="true">
  <path d="M82 410 V44 Q82 20 106 20 H290 Q320 20 335 45 Q352 82 395 84 H845 Q874 84 874 112 V410 Z" fill="#fff"/>
</svg>

<nav class="abs utility-links">Home <span>|</span> Contact Us <span>|</span> Sitemap</nav>
<svg class="abs phone-icon" width="40" height="40" viewBox="0 0 40 40" aria-hidden="true">
  <circle cx="20" cy="20" r="17" fill="none" stroke="#fff" stroke-width="2.5"/>
  <path d="M15 9 h5 l1 6 -3 2 q2 5 6 7 l2-3 6 1 v5 q-12 1-17-18z" fill="#fff"/>
</svg>
<div class="abs phones">Lease (48) 3100-2040<br>Sales: (48) 9120-455</div>

<div class="abs brand">Casalúmen</div>

<nav class="abs main-nav">
  <a class="active">The company</a><a>Location</a><a>Restricted Area</a><a>List your property</a><a>Owner Info</a><a>Information for Tenant</a><a>Request your property</a>
</nav>

<div class="abs hero" role="img" aria-label="Photo of a lit pool house at dusk with a pool and sun loungers"></div>
<div class="abs hero-shadow"></div>

<h2 class="abs welcome-title"><span class="w">W</span>elcome <em>Message</em></h2>
<div class="abs dotted" style="left:108px;top:582px;width:482px"></div>
<div class="abs welcome-text">
  <p>The Casalúmen, for over fifteen years in the real estate market, permeated the culture and values defined by the needs of its customers, is gradually building a solid body for the management and sale of real estate. These years marked by moments of achievement and adversity, brought him the wisdom necessary to build step by step a large gap in the provision of its services.Bring happiness to relationships, provide solidity to the continuing purpose of serving, has been objectively the character of their actions.</p>
  <p>&nbsp; Movements in search of a personalized service have the convenience of the Customer, its greater purpose. Has been its commitment to sustain permanently ethical management, fully honoring all financial commitments and tax, making transparent the relationship with clients, be they owners,</p>
</div>
<div class="abs contact-line"><span class="big">(48) 9120-4551</span><span class="small">Or Email us @</span><span class="mail">info@casalumen.com.br</span></div>

<section class="abs map-box">
  <h3>Search <b>PROPERTY</b> by region</h3>
  <div class="abs map" role="img" aria-label="Regional map of the island and coast for searching properties by region"></div>
</section>

<div class="abs divider"></div>

<h3 class="abs col-title" style="left:110px;top:846px">The Company</h3>
<div class="abs dotted" style="left:108px;top:886px;width:216px"></div>
<div class="abs company-photo"><div role="img" aria-label="Photo of a hand holding a small model house"></div></div>
<p class="abs col-text" style="left:106px;top:998px;width:218px"><b>This is a complete list of all the projects that the</b> Foundation has funded, starting with the most recent. (The organisation named is the one we funded to do the work.) To be more selective, use the facility on the right...</p>
<span class="abs details" style="left:246px;top:1082px">Click for details...</span>

<div class="abs col-sep" style="left:342px"></div>
<h3 class="abs col-title" style="left:362px;top:849px">Information for Tenant</h3>
<div class="abs dotted" style="left:365px;top:886px;width:213px"></div>
<div class="abs col-text" style="left:358px;top:898px;width:218px">
  <p><b>This is a complete listing of all the reports pub-</b>lished with the Foundation's support, starting with the most recent. To be more selective, use the facilities on the right to search by report type or to list all reports for a particular month or year. Please press 'Reset' between multiple searches.</p>
  <p style="margin-top:16px">You may download, store and use these for your own personal use and research, or that of your charity, company or organisation.....</p>
</div>
<span class="abs details" style="left:503px;top:1082px">Click for details...</span>

<div class="abs col-sep" style="left:598px"></div>
<h3 class="abs col-title" style="left:621px;top:846px">Search for properties</h3>
<div class="abs dotted" style="left:620px;top:886px;width:212px"></div>
<p class="abs col-text" style="left:631px;top:898px;width:232px;text-align:left">Lorem Ipsum is simply dummy text of the printing and typesetting industry.</p>
<div class="abs radio" style="top:948px"><i></i>To buy</div>
<div class="abs radio" style="top:972px"><i class="on"></i>Rent</div>
<div class="abs select">Every</div>
<div class="abs btn-search">
  <svg width="18" height="14" viewBox="0 0 18 14" aria-hidden="true"><circle cx="6" cy="7" r="5" fill="none" stroke="#fff" stroke-width="1.5"/><path d="M10 9 l6 4" stroke="#fff" stroke-width="2"/></svg>Buscar
</div>

<footer class="abs footer">
  Rua das Acácias, 118 - Corner with Avenida Lumiar - Centro Florianopolis -<br>
  CEP: 88015-300 - Fax: (48) 3100-2099<br>
  (C) 2013 - Casalúmen - All rights reserved.
</footer>
</body>
</html>
```